Stationary design for new digital markerting company

I need a stationary design for a new digital marketing company called Lofty Wren.
We work with businesses to help them create and increase their online presence in order to increase awareness of their brand.
The design must keep with the colour schemes of our logo.
I would like a design that stands out but isn't over the top while also being professional and sophisticated.

Target Market(s)

other businesses

Industry/Entity Type

Business Consultant

Font styles to use
Sans Serif

Colors
abd036
ffffff
a54499

Requirements
Must have
• logo, plus the same colour scheme

```html
<!DOCTYPE html>
<html lang="en">
<head>
<meta charset="utf-8">
<title>Lofty Wren — Stationery</title>
<link rel="stylesheet" href="https://fonts.googleapis.com/css2?family=Montserrat:wght@400;600;700&display=swap">
<style>
  :root {
    --purple: #8a2278;
    --purple-deep: #7a1f6b;
    --green: #8cb82b;
    --paper: #ffffff;
    --backdrop: #ececec;
    --ink: #555555;
    --ink-soft: #8a8a8a;
  }
  * { box-sizing: border-box; margin: 0; padding: 0; }
  html, body { width: 1200px; height: 884px; overflow: hidden; }
  body {
    position: relative;
    background: var(--backdrop);
    font-family: "Montserrat", sans-serif;
    color: var(--ink);
  }
  .sheet {
    position: absolute;
    background: var(--paper);
    box-shadow: 0 2px 8px rgba(0,0,0,.12);
    overflow: hidden;
  }
  .brand {
    display: flex;
    align-items: center;
    gap: 6px;
    color: var(--purple);
    font-weight: 700;
    letter-spacing: .04em;
    text-transform: uppercase;
    white-space: nowrap;
  }
  .brand-dot {
    display: inline-block;
    border-radius: 50%;
    background: var(--green);
    flex: none;
  }
  .brand--on-dark { color: var(--paper); }

  /* Letterhead */
  .letterhead { left: 40px; top: 40px; width: 330px; height: 467px; }
  .letterhead .brand { position: absolute; left: 26px; top: 34px; font-size: 13px; }
  .letterhead .brand-dot { width: 16px; height: 16px; }
  .letter-body { position: absolute; left: 26px; top: 84px; right: 26px; font-size: 7px; line-height: 1.55; }
  .letter-body p { margin-bottom: 8px; }
  .letter-sign { margin-top: 14px; }
  .letter-sign strong { display: block; color: var(--purple); font-weight: 600; }
  .letter-footer {
    position: absolute; left: 0; right: 0; bottom: 0; height: 30px;
    background: var(--purple); border-bottom: 6px solid var(--green);
    color: var(--paper); font-size: 6.5px;
    display: flex; align-items: center; justify-content: space-around; padding: 0 14px;
  }

  /* Folder */
  .folder { left: 400px; top: 40px; width: 330px; height: 467px; }
  .folder .brand { position: absolute; left: 28px; top: 52px; font-size: 17px; }
  .folder .brand-dot { width: 22px; height: 22px; }
  .folder-panel { position: absolute; left: 0; right: 0; top: 150px; height: 230px; background: var(--purple); }
  .folder-band {
    position: absolute; left: 0; right: 0; top: 380px; bottom: 0; background: var(--green);
    color: var(--paper); font-size: 8px; display: flex; align-items: center; justify-content: flex-end; padding-right: 24px;
  }

  /* Envelope */
  .envelope { left: 760px; top: 40px; width: 400px; height: 200px; }
  .envelope-flap { position: absolute; left: 0; right: 0; top: 0; height: 70px; background: var(--purple); border-radius: 0 0 14px 14px; }
  .envelope-seal { position: absolute; left: 192px; top: 28px; width: 16px; height: 16px; border-radius: 50%; background: var(--green); }

  /* Compliment slip */
  .slip { left: 760px; top: 270px; width: 400px; height: 200px; }
  .slip .brand { position: absolute; left: 24px; top: 96px; font-size: 15px; }
  .slip .brand-dot { width: 20px; height: 20px; }
  .slip-footer {
    position: absolute; left: 0; right: 0; bottom: 0; height: 28px; background: var(--purple);
    border-bottom: 6px solid var(--green); color: var(--paper); font-size: 7px;
    display: flex; align-items: center; padding-left: 24px;
  }

  /* Business cards */
  .card { width: 190px; height: 106px; top: 500px; }
  .card--front { left: 760px; background: var(--purple); display: flex; align-items: center; justify-content: center; }
  .card--front .brand { font-size: 12px; }
  .card--front .brand-dot { width: 15px; height: 15px; }
  .card--back { left: 970px; }
  .card--back .brand { position: absolute; left: 12px; top: 14px; font-size: 9px; }
  .card--back .brand-dot { width: 11px; height: 11px; }
  .card-person { position: absolute; right: 12px; top: 12px; text-align: right; font-size: 8px; color: var(--green); font-weight: 600; }
  .card-person span { display: block; color: var(--ink-soft); font-size: 6px; font-weight: 400; }
  .card-contact {
    position: absolute; left: 0; right: 0; bottom: 0; height: 46px; background: var(--purple);
    border-bottom: 5px solid var(--green); color: var(--paper); font-size: 6px; line-height: 1.5;
    display: flex; justify-content: space-between; padding: 8px 12px;
  }

  /* Notebook */
  .notebook { left: 400px; top: 540px; width: 260px; height: 320px; padding-left: 0; }
  .notebook .brand { position: absolute; left: 30px; top: 40px; font-size: 14px; }
  .notebook .brand-dot { width: 18px; height: 18px; }
  .notebook-panel { position: absolute; left: 0; right: 0; top: 108px; height: 150px; background: var(--purple); }
  .notebook-band {
    position: absolute; left: 0; right: 0; top: 258px; bottom: 0; background: var(--green);
    color: var(--paper); font-size: 7px; display: flex; align-items: center; justify-content: flex-end; padding-right: 16px;
  }
  .notebook-binding { position: absolute; left: 6px; top: 10px; bottom: 10px; width: 10px; }

  /* Key tag & eraser */
  .key-tag { left: 700px; top: 640px; width: 130px; height: 70px; border-radius: 8px; display: flex; align-items: center; justify-content: center; }
  .key-tag .brand { font-size: 10px; }
  .key-tag .brand-dot { width: 12px; height: 12px; }
  .key-ring { position: absolute; left: 745px; top: 600px; }
  .eraser { left: 860px; top: 650px; width: 110px; height: 50px; background: var(--purple); border-left: 22px solid var(--paper); display: flex; align-items: center; justify-content: center; }
  .eraser .brand { font-size: 8px; }
  .eraser .brand-dot { width: 10px; height: 10px; }
</style>
</head>
<body>

<article class="sheet letterhead">
  <div class="brand"><span class="brand-dot"></span>Lofty Wren</div>
  <div class="letter-body">
    <p>Recipient's Name<br>12 Harbour Lane<br>Portmere 4021</p>
    <p>Dear Sir,</p>
    <p>Thank you for meeting with our team last week. We have outlined a plan to grow your online presence and lift awareness of your brand across search and social channels.</p>
    <p>The attached proposal sets out timelines, costs and the results you can expect in the first quarter. Please review it at your convenience.</p>
    <p>We look forward to working with you.</p>
    <div class="letter-sign">Yours sincerely,<strong>Maya Lorne</strong>Director</div>
  </div>
  <footer class="letter-footer">
    <span>Level 8, 21 Quay Street, Portmere</span>
    <span>0400 123 456</span>
    <span>hello@loftywren.com</span>
    <span>www.loftywren.com</span>
  </footer>
</article>

<article class="sheet folder">
  <div class="brand"><span class="brand-dot"></span>Lofty Wren</div>
  <div class="folder-panel"></div>
  <div class="folder-band">www.loftywren.com</div>
</article>

<article class="sheet envelope">
  <div class="envelope-flap"></div>
  <span class="envelope-seal"></span>
</article>

<article class="sheet slip">
  <div class="brand"><span class="brand-dot"></span>Lofty Wren</div>
  <footer class="slip-footer">Level 8, 21 Quay Street, Portmere</footer>
</article>

<article class="sheet card card--front">
  <div class="brand brand--on-dark"><span class="brand-dot"></span>Lofty Wren</div>
</article>

<article class="sheet card card--back">
  <div class="brand"><span class="brand-dot"></span>Lofty Wren</div>
  <div class="card-person">Sam Carver<span>Managing Director</span></div>
  <div class="card-contact">
    <span>Level 8, 21 Quay Street<br>Portmere</span>
    <span>0400 123 456<br>hello@loftywren.com<br>www.loftywren.com</span>
  </div>
</article>

<article class="sheet notebook">
  <svg class="notebook-binding" viewBox="0 0 10 300" preserveAspectRatio="none" aria-hidden="true">
    <line x1="5" y1="0" x2="5" y2="300" stroke="#444" stroke-width="3" stroke-dasharray="4 8"/>
  </svg>
  <div class="brand"><span class="brand-dot"></span>Lofty Wren</div>
  <div class="notebook-panel"></div>
  <div class="notebook-band">www.loftywren.com</div>
</article>

<svg class="key-ring" style="position:absolute" width="40" height="44" viewBox="0 0 40 44" aria-hidden="true">
  <circle cx="20" cy="16" r="13" fill="none" stroke="#9a9a9a" stroke-width="2.5"/>
  <line x1="20" y1="29" x2="20" y2="42" stroke="#9a9a9a" stroke-width="2"/>
</svg>
<div class="sheet key-tag">
  <div class="brand"><span class="brand-dot"></span>Lofty Wren</div>
</div>

<div class="sheet eraser">
  <div class="brand brand--on-dark"><span class="brand-dot"></span>Lofty Wren</div>
</div>

</body>
</html>
```